I need a fresh looking, exciting and loaded design for Full service Restaurant

We need a web design for our restaurant, which offers full service Pakistani and Indian food in PA, USA. Design should be elegant, simplified so customers can navigate easily and order food online for catering as well as delivery. We need loads of pictures and room to grow. I already have a web address via vexlorin.com. It should include SSL and e-commerce for ordering food.
Be original and be creative and make it a fun site :)

Industry/Entity Type

Restaurant

```html
<!DOCTYPE html>
<html lang="en">
<head>
<meta charset="utf-8">
<title>Saffron Lane – A fine Pak-Indian Cuisine</title>
<link href="https://fonts.googleapis.com/css2?family=Lobster&family=Open+Sans:wght@400;600&display=swap" rel="stylesheet">
<style>
:root{
  --red:#c8171c;
  --green:#2f6a12;
  --text:#555555;
  --heading:#222222;
  --light:#f1f1f1;
  --white:#ffffff;
  --footer:#1d1d1d;
  --footer-bar:#111111;
  --footer-text:#d8d8d8;
}
*{margin:0;padding:0;box-sizing:border-box}
html,body{width:1200px;height:2267px;overflow:hidden}
body{position:relative;background:var(--white);font-family:"Open Sans",Arial,sans-serif;color:var(--text)}
.abs{position:absolute}

/* header */
.top-line{left:0;top:0;width:1200px;height:4px;background:var(--green)}
.brand{left:100px;top:42px;display:flex;align-items:center;gap:10px}
.brand-dot{width:34px;height:34px;border-radius:50%;background:var(--red)}
.brand-name{font-family:"Lobster",cursive;font-size:34px;color:var(--red);line-height:1}
.brand-tag{left:146px;top:82px;font-size:11px;color:var(--green);font-weight:600}
.header-phone{right:110px;top:55px;display:flex;align-items:center;gap:8px;font-family:"Lobster",cursive;font-size:17px;color:var(--red)}
.phone-ring{width:30px;height:30px;border:1.5px solid var(--green);border-radius:50%;display:flex;align-items:center;justify-content:center}

/* hero */
.hero{left:0;top:151px;width:1200px;height:514px;
  background:radial-gradient(ellipse at 40% 55%,#c7a06a 0%,#b5804f 22%,#e9e6df 48%,#f3f1ec 70%,#dcdad3 100%)}
.nav-band{left:0;top:138px;width:1200px;height:46px;background:var(--red)}
.nav{left:380px;top:138px;height:46px;display:flex;align-items:center}
.nav a{font-family:"Lobster",cursive;color:var(--white);text-decoration:none;font-size:16px;margin-right:62px}
.hero-brand{left:0;top:350px;width:1200px;text-align:center;font-family:"Lobster",cursive;font-size:38px;color:var(--white)}
.hero-copy{left:410px;top:408px;width:380px;text-align:center;font-size:12.8px;line-height:24px;color:var(--white)}
.btn{display:flex;align-items:center;justify-content:center;background:var(--red);color:var(--white);font-size:13px;border-radius:3px}
.hero-btn{left:536px;top:487px;width:129px;height:42px}
.arrow{top:385px;width:16px;height:50px}

/* welcome */
.welcome-img{left:103px;top:725px;width:335px;height:238px;border:5px solid var(--white);box-shadow:0 0 0 1px #cfcfcf,0 2px 6px rgba(0,0,0,.2);
  background:linear-gradient(135deg,#b8742f 0%,#8a3a1e 40%,#d9c9a8 70%,#efe8dc 100%)}
.section-title{font-family:"Lobster",cursive;color:var(--red);font-size:31px;display:flex;align-items:center;gap:10px;font-weight:400}
.title-dot{width:26px;height:26px;border-radius:50%;background:var(--red)}
.welcome-title{left:456px;top:740px}
.welcome-copy{left:456px;top:789px;width:650px;font-size:12.7px;line-height:24px}
.welcome-btn{left:456px;top:919px;width:129px;height:42px}

/* featured */
.featured{left:0;top:1024px;width:1200px;height:573px;background:var(--light);border-top:1px solid #e2e2e2;border-bottom:1px solid #e2e2e2}
.center-title{left:0;width:1200px;justify-content:center}
.card{top:1153px;width:317px;height:396px;background:var(--white)}
.card-img{width:317px;height:207px}
.card-title{position:absolute;left:18px;top:218px;font-family:"Lobster",cursive;font-size:17px;color:var(--heading);font-weight:400}
.card-copy{position:absolute;left:18px;top:245px;width:292px;font-size:12.4px;line-height:24px}
.read-more{font-size:12px;color:var(--red)}
.card .read-more{position:absolute;left:20px;top:345px}

/* events */
.event-img{top:1726px;width:166px;height:133px;border:4px solid var(--white);box-shadow:0 0 0 1px #cfcfcf,0 2px 5px rgba(0,0,0,.2)}
.event-body{top:1722px;width:300px}
.event-title{font-family:"Lobster",cursive;font-size:17px;color:var(--heading);font-weight:400}
.event-date{font-size:12px;margin:6px 0 4px;display:flex;align-items:center;gap:8px}
.event-copy{font-size:13px;line-height:21px}

/* footer */
.footer{left:0;top:1907px;width:1200px;height:311px;background:var(--footer)}
.footer-bar{left:0;top:2218px;width:1200px;height:49px;background:var(--footer-bar)}
.footer-heading{font-family:"Lobster",cursive;font-size:19px;color:var(--white);font-weight:400}
.contact-list{left:100px;top:1995px;width:260px;color:var(--white);font-size:14px}
.contact-row{display:flex;gap:20px;align-items:flex-start;margin-bottom:10px}
.contact-row .icon{width:22px;flex:none;display:flex;justify-content:center}
.contact-label{text-transform:uppercase;font-size:15px;letter-spacing:.3px}
.contact-val{font-size:13px;line-height:20px;color:var(--footer-text);margin-top:4px}
.map{left:373px;top:1987px;width:410px;height:204px;border-radius:4px;
  background:linear-gradient(160deg,#e7e1d2 0%,#d9dcc6 35%,#c9d8b6 60%,#e6dfcc 100%)}
.news-copy{left:842px;top:1987px;width:265px;font-size:11px;line-height:18px;color:var(--footer-text)}
.field{left:842px;width:263px;height:40px;background:#f3f3f3;border-radius:2px;font-size:11px;color:#444;padding-left:14px;display:flex;align-items:center}
.signup{left:842px;top:2143px;width:263px;height:38px;font-size:13px;text-transform:uppercase}
.copyright{left:102px;top:2236px;font-size:12px;color:var(--footer-text)}
.social{left:936px;top:2230px;display:flex;gap:8px}
.social span{width:27px;height:27px;border:1.5px solid #cfcfcf;border-radius:50%}
</style>
</head>
<body>

<div class="abs top-line"></div>

<div class="abs hero" role="img" aria-label="Photograph of chaat topped with sev and chutney on a white plate, with green chillies, a lime and a bowl of tamarind sauce"></div>

<div class="abs nav-band"></div>

<div class="abs brand">
  <span class="brand-dot"></span>
  <span class="brand-name">Saffron Lane</span>
</div>
<div class="abs brand-tag">A fine Pak-Indian Cuisine</div>

<div class="abs header-phone">
  <span class="phone-ring">
    <svg width="14" height="14" viewBox="0 0 24 24"><path d="M6.6 10.8a15 15 0 0 0 6.6 6.6l2.2-2.2c.3-.3.7-.4 1-.2 1.1.4 2.3.6 3.6.6.6 0 1 .4 1 1V20c0 .6-.4 1-1 1A17 17 0 0 1 3 4c0-.6.4-1 1-1h3.5c.6 0 1 .4 1 1 0 1.3.2 2.5.6 3.6.1.3 0 .7-.2 1z" fill="var(--green)"/></svg>
  </span>
  +1 415 555 0148
</div>

<nav class="abs nav">
  <a href="#">Home</a><a href="#">Features</a><a href="#">Our Menus</a><a href="#">Events</a><a href="#">Our Services</a><a href="#">Contact</a>
</nav>

<div class="abs hero-brand">Saffron Lane</div>
<p class="abs hero-copy">Lorem Ipsum is simply dummy text of the printing and typesetting industry. Lorem Ipsum has been the industry's standard dummy text</p>
<a class="abs btn hero-btn">View more</a>
<svg class="abs arrow" style="left:40px" viewBox="0 0 16 50"><path d="M14 2 L2 25 L14 48" fill="none" stroke="#888" stroke-width="1.5"/></svg>
<svg class="abs arrow" style="left:1144px" viewBox="0 0 16 50"><path d="M2 2 L14 25 L2 48" fill="none" stroke="#888" stroke-width="1.5"/></svg>

<!-- welcome -->
<div class="abs welcome-img" role="img" aria-label="Photograph of the restaurant dining room with set tables and chandeliers"></div>
<h2 class="abs section-title welcome-title"><span class="title-dot"></span>Welcome to Saffron Lane</h2>
<p class="abs welcome-copy">Lorem Ipsum is simply dummy text of the printing and typesetting industry. Lorem Ipsum has been the industry's standard dummy text ever since the 1500s, when an unknown printer took a galley of type and scrambled it to make a type specimen book. It has survived not only five centuries, but also the leap into electronic typesetting, remaining essentially unchanged.Lorem Ipsum is simply dummy text of the printing and typesetting industry. Lorem Ipsum has been the industry's</p>
<a class="abs btn welcome-btn">View more</a>

<!-- featured -->
<div class="abs featured"></div>
<h2 class="abs section-title center-title" style="top:1078px"><span class="title-dot"></span>Our Featured Dishes</h2>

<article class="abs card" style="left:100px">
  <div class="card-img" role="img" aria-label="Photograph of curries, rice and naan in copper bowls" style="background:linear-gradient(135deg,#c98a3a,#e7c55a 45%,#8a4a22)"></div>
  <h3 class="card-title">Finibus Bonorum et Malorum</h3>
  <p class="card-copy">Lorem Ipsum is simply dummy text of the printing and typesetting industry. Lorem Ipsum has been the industry's standard dummy text ever</p>
  <a class="read-more">Read more &gt;&gt;</a>
</article>
<article class="abs card" style="left:441px">
  <div class="card-img" role="img" aria-label="Photograph of a thali platter with small bowls and flatbread" style="background:linear-gradient(135deg,#5a3a24,#c9a46a 45%,#8f8f88)"></div>
  <h3 class="card-title">Remaining essentially</h3>
  <p class="card-copy">Lorem Ipsum is simply dummy text of the printing and typesetting industry. Lorem Ipsum has been the industry's standard dummy text ever</p>
  <a class="read-more">Read more &gt;&gt;</a>
</article>
<article class="abs card" style="left:783px">
  <div class="card-img" role="img" aria-label="Photograph of a colourful salad platter with spices on a dark table" style="background:linear-gradient(135deg,#3d3630,#d6512f 45%,#6a8a3a)"></div>
  <h3 class="card-title">Our Featured Dishes</h3>
  <p class="card-copy">Lorem Ipsum is simply dummy text of the printing and typesetting industry. Lorem Ipsum has been the industry's standard dummy text ever</p>
  <a class="read-more">Read more &gt;&gt;</a>
</article>

<!-- events -->
<h2 class="abs section-title center-title" style="top:1656px"><span class="title-dot"></span>Latest events</h2>

<div class="abs event-img" style="left:98px;background:linear-gradient(160deg,#9fb4c8,#c79a6a 60%,#6b4a2e)" role="img" aria-label="Photograph of a city landmark with dishes in the foreground"></div>
<div class="abs event-body" style="left:284px">
  <h3 class="event-title">The standard Lorem Ipsum passage</h3>
  <div class="event-date"><svg width="12" height="12" viewBox="0 0 12 12"><rect x="1" y="2" width="10" height="9" fill="none" stroke="#555"/><path d="M1 5h10M4 1v2M8 1v2" stroke="#555"/></svg>March 23,2014</div>
  <p class="event-copy">Lorem Ipsum is simply dummy text of the printing and typesetting industry. Lorem Ipsum has been the industry's standard dummy</p>
  <a class="read-more">Read more &gt;&gt;</a>
</div>

<div class="abs event-img" style="left:604px;background:linear-gradient(160deg,#f0ede8,#9a3a1e 50%,#e8e4dc)" role="img" aria-label="Photograph of a bowl of meat curry"></div>
<div class="abs event-body" style="left:790px">
  <h3 class="event-title">Standard dummy text</h3>
  <div class="event-date"><svg width="12" height="12" viewBox="0 0 12 12"><rect x="1" y="2" width="10" height="9" fill="none" stroke="#555"/><path d="M1 5h10M4 1v2M8 1v2" stroke="#555"/></svg>March 23,2014</div>
  <p class="event-copy">Lorem Ipsum is simply dummy text of the printing and typesetting industry. Lorem Ipsum has been the industry's standard dummy</p>
  <a class="read-more">Read more &gt;&gt;</a>
</div>

<!-- footer -->
<footer class="abs footer"></footer>
<h4 class="abs footer-heading" style="left:100px;top:1944px">Contact Us</h4>
<h4 class="abs footer-heading" style="left:367px;top:1944px">Location Map</h4>
<h4 class="abs footer-heading" style="left:840px;top:1944px">Sign up for newsletter</h4>

<div class="abs contact-list">
  <div class="contact-row">
    <span class="icon"><svg width="14" height="18" viewBox="0 0 14 18"><path d="M7 0a7 7 0 0 0-7 7c0 5 7 11 7 11s7-6 7-11a7 7 0 0 0-7-7zm0 10a3 3 0 1 1 0-6 3 3 0 0 1 0 6z" fill="#fff"/></svg></span>
    <div><div class="contact-label">Address</div><div class="contact-val">42 Amber Rd, Millbrook<br>PA 19020,Philadelphia</div></div>
  </div>
  <div class="contact-row">
    <span class="icon"><svg width="16" height="16" viewBox="0 0 24 24"><path d="M6.6 10.8a15 15 0 0 0 6.6 6.6l2.2-2.2c.3-.3.7-.4 1-.2 1.1.4 2.3.6 3.6.6.6 0 1 .4 1 1V20c0 .6-.4 1-1 1A17 17 0 0 1 3 4c0-.6.4-1 1-1h3.5c.6 0 1 .4 1 1 0 1.3.2 2.5.6 3.6.1.3 0 .7-.2 1z" fill="#fff"/></svg></span>
    <div><div class="contact-label">Call us</div><div class="contact-val" style="font-size:14px;margin-top:10px">+1 903-555-0172</div></div>
  </div>
  <div class="contact-row">
    <span class="icon"><svg width="18" height="14" viewBox="0 0 18 14"><rect x="1" y="1" width="16" height="12" fill="none" stroke="#fff" stroke-width="1.5"/><path d="M1 1l8 7 8-7" fill="none" stroke="#fff" stroke-width="1.5"/></svg></span>
    <div><div class="contact-label">E - Mail</div><div class="contact-val" style="margin-top:10px">info@saffronlane.com</div></div>
  </div>
</div>

<div class="abs map" role="img" aria-label="Street map showing the restaurant location"></div>

<p class="abs news-copy">Excepteur sint occaecat cupidatat non proident, sunt in culpa qui officia deserunt</p>
<div class="abs field" style="top:2043px">Enter Name</div>
<div class="abs field" style="top:2094px">Email</div>
<a class="abs btn signup">Sign up now</a>

<div class="abs footer-bar"></div>
<p class="abs copyright">Copyright 2015 Saffron Lane . All Rights Reserved</p>
<div class="abs social"><span></span><span></span><span></span><span></span><span></span></div>

</body>
</html>
```